Zielgruppe
Tobias Fink Personal Training.
Personaltraining für Bürotätige / leitende Positionen.
Rücken- und Haltungstraining.
Zielgruppe: Herren mittleren Alters, gehobene Klasse.
Aufgabenstellung
Schlicht, elegant, hochwertig
Gerne Logo eingearbeitet.
Schwarz / Gold / Weiß

```html
<!DOCTYPE html>
<html lang="de">
<head>
<meta charset="utf-8">
<title>Tobias Fink Personal Training – Visitenkarte</title>
<link rel="stylesheet" href="https://fonts.googleapis.com/css2?family=Open+Sans:wght@400;600&display=swap">
<style>
  :root {
    --page: #dcdfe2;
    --slate: #2c373f;
    --gold: #c9a227;
    --white: #ffffff;
    --text-light: #e9edf0;
    --text-muted: #b7c0c7;
  }
  * { box-sizing: border-box; margin: 0; padding: 0; }
  html, body {
    width: 1200px; height: 900px; overflow: hidden;
    background: var(--page);
    font-family: "Open Sans", Arial, sans-serif;
  }
  .card {
    position: absolute; left: 290px;
    width: 620px; height: 354px;
    background: var(--slate);
    overflow: hidden;
    box-shadow: 0 10px 30px rgba(0,0,0,.18);
  }

  /* neutral name placeholder: one colour, one weight, one plain square */
  .brand-name {
    display: flex; align-items: center; gap: 12px;
    color: var(--gold); font-weight: 600;
  }
  .brand-name__square {
    flex: none; background: var(--gold);
  }

  /* front side */
  .card--front { top: 66px; }
  .front__brand {
    position: absolute; left: 0; right: 0; top: 140px;
    justify-content: center;
    font-size: 30px; line-height: 1.2; letter-spacing: .5px;
  }
  .front__brand .brand-name__square { width: 18px; height: 18px; }
  .front__web {
    position: absolute; left: 0; right: 0; bottom: 54px;
    display: flex; justify-content: center; align-items: center; gap: 8px;
    font-size: 15px; color: var(--text-light);
  }

  /* back side */
  .card--back { top: 480px; }
  .back__brand-panel {
    position: absolute; left: 0; top: 0; bottom: 0; width: 248px;
    background: var(--white);
    display: flex; align-items: center; justify-content: center;
    padding: 0 24px;
  }
  .back__brand-panel .brand-name {
    font-size: 19px; line-height: 1.3; gap: 10px;
  }
  .back__brand-panel .brand-name__square { width: 12px; height: 12px; }
  .back__accent {
    position: absolute; left: 256px; top: 70px;
    width: 8px; height: 150px; border-radius: 4px;
    background: var(--gold);
  }
  .back__details {
    position: absolute; left: 300px; top: 62px;
    color: var(--text-light);
  }
  .person__name { font-size: 22px; font-weight: 600; }
  .person__role { font-size: 12px; color: var(--text-muted); margin-bottom: 18px; }
  .company { font-size: 15px; line-height: 1.4; margin-bottom: 16px; }
  .contact { list-style: none; font-size: 15px; line-height: 1.6; }
  .contact li { display: flex; align-items: center; gap: 10px; }
  .contact svg { width: 14px; height: 14px; flex: none; }
</style>
</head>
<body>

<section class="card card--front">
  <div class="brand-name front__brand">
    <span class="brand-name__square"></span>
    <span>Tobias Fink Personal Training</span>
  </div>
  <div class="front__web">
    <svg width="14" height="14" viewBox="0 0 16 16" fill="none" stroke="#e9edf0" stroke-width="1.4">
      <circle cx="8" cy="8" r="6.5"/><ellipse cx="8" cy="8" rx="2.8" ry="6.5"/><line x1="1.5" y1="8" x2="14.5" y2="8"/>
    </svg>
    www.tfpt-beispiel.at
  </div>
</section>

<section class="card card--back">
  <div class="back__brand-panel">
    <div class="brand-name">
      <span class="brand-name__square"></span>
      <span>Tobias Fink<br>Personal Training</span>
    </div>
  </div>
  <div class="back__accent"></div>
  <div class="back__details">
    <div class="person__name">Jonas Berger</div>
    <div class="person__role">Geschäftsführer</div>
    <div class="company">TFPT GmbH<br>Lindenweg 14/3<br>8010 Graz</div>
    <ul class="contact">
      <li>
        <svg viewBox="0 0 16 16" fill="#c9a227"><path d="M3 1h3l1.5 4-2 1.3a9 9 0 0 0 4.2 4.2L11 8.5l4 1.5v3a2 2 0 0 1-2 2A12 12 0 0 1 1 3a2 2 0 0 1 2-2z"/></svg>
        +43 660 480 21 37
      </li>
      <li>
        <svg viewBox="0 0 16 16" fill="#c9a227"><rect x="4" y="1" width="8" height="5"/><rect x="1" y="6" width="14" height="6" rx="1"/><rect x="4" y="10" width="8" height="5" fill="#fff"/></svg>
        +43 660 480 21 38
      </li>
      <li>
        <svg viewBox="0 0 16 16"><rect x="1" y="3" width="14" height="10" fill="#c9a227"/><path d="M1 3l7 6 7-6" fill="none" stroke="#2c373f" stroke-width="1.4"/></svg>
        office@tfpt-beispiel.at
      </li>
    </ul>
  </div>
</section>

</body>
</html>
```